Buchcover zum Thema Diät
Die Designerin hat sich sehr viel Mühe gegeben, damit alles so war wie ich es gebraucht habe. Sie hat auf meine Fragen auch immer schnell geantwortet. Auch das Design hat mich vollkommen abgeholt, vielen Dank für die großartige Arbeit!
Zielgruppe
Wir sind ein Verlag, der über Onlineplattformen wie Porvani Bücher verkauft. Unsere Zielgruppe sind mehrheitlich Frauen zwischen 25 und 55.
Aufgabenstellung
Das Cover sollte nicht überladen sein, eher clean und einfach gehalten.
Buchtitel: Leichter leben mit der Velorin Diät – ganz einfach!
Nebentitel: Gesunde und leckere Rezepte für jede Tageszeit inkl. 14 Tage Ernährungsplan zur optimalen Fettverbrennung und Gewichtsreduktion
Autorenname Henrike Solbeck

```html
<!DOCTYPE html>
<html lang="de">
<head>
<meta charset="utf-8">
<title>Leichter leben mit der Velorin Diät – Buchumschlag</title>
<link rel="stylesheet" href="https://fonts.googleapis.com/css2?family=Inter:wght@700;800;900&family=Arimo:wght@400&display=swap">
<style>
  :root {
    --sage: #a3ad95;
    --sage-light: #b9c2ad;
    --sage-pale: #cbd1c0;
    --skin: #d9c9b6;
    --skin-shade: #c4b49f;
    --cloth: #8f9989;
    --white: #ffffff;
    --trim: #1b1b1b;
    --fold: #2f8fd6;
  }
  * { margin: 0; padding: 0; box-sizing: border-box; }
  html, body { width: 1200px; height: 597px; overflow: hidden; background: var(--sage); }
  .cover {
    position: relative; width: 1200px; height: 597px; overflow: hidden;
    background: var(--sage); color: var(--white);
    font-family: "Inter", "Helvetica Neue", Arial, sans-serif;
  }
  .trim-frame {
    position: absolute; left: 8px; top: 9px; width: 1182px; height: 580px;
    border: 1px solid var(--trim); z-index: 3; pointer-events: none;
  }
  .fold-line {
    position: absolute; top: 0; height: 597px; width: 0;
    border-left: 1px dashed var(--fold);
  }
  .fold-line.left { left: 588px; }
  .fold-line.right { left: 611px; }

  /* Back */
  .back {
    position: absolute; left: 24px; top: 60px; width: 550px; text-align: center;
  }
  .back-heading {
    font-family: "Inter", Arial, sans-serif; font-weight: 700;
    font-size: 16px; letter-spacing: 0.1px; margin-bottom: 22px;
  }
  .back-text {
    font-family: "Arimo", Arial, sans-serif; font-weight: 400;
    font-size: 17px; line-height: 20.5px; margin-bottom: 21px;
  }
  .back-text.spaced { margin-top: 40px; }

  /* Spine */
  .spine-text {
    position: absolute; writing-mode: vertical-rl; transform: rotate(180deg);
    font-weight: 800; letter-spacing: 0.3px; white-space: nowrap;
    left: 594px;
  }
  .spine-author { top: 50px; font-size: 11px; }
  .spine-title { bottom: 40px; font-size: 11px; }

  /* Front */
  .cover-photo {
    position: absolute; left: 930px; top: 20px; width: 262px; height: 540px;
    background:
      radial-gradient(ellipse 30% 9% at 62% 11%, var(--skin) 0%, rgba(217,201,182,0) 100%),
      radial-gradient(ellipse 32% 9% at 64% 26%, var(--cloth) 0%, rgba(143,153,137,0) 100%),
      radial-gradient(ellipse 28% 10% at 62% 40%, var(--skin) 0%, rgba(217,201,182,0) 100%),
      radial-gradient(ellipse 32% 8% at 60% 56%, var(--cloth) 0%, rgba(143,153,137,0) 100%),
      radial-gradient(ellipse 30% 22% at 55% 78%, var(--skin-shade) 0%, rgba(196,180,159,0) 100%),
      radial-gradient(ellipse 60% 55% at 55% 45%, var(--sage-pale) 0%, var(--sage-light) 55%, rgba(163,173,149,0) 100%);
    -webkit-mask-image: linear-gradient(to bottom, #000 80%, transparent 100%);
    mask-image: linear-gradient(to bottom, #000 80%, transparent 100%);
  }
  .author {
    position: absolute; left: 649px; top: 47px; z-index: 2;
    font-weight: 800; font-size: 15px; letter-spacing: 0.2px;
  }
  .title {
    position: absolute; left: 647px; top: 86px; z-index: 2;
    font-weight: 900; font-size: 52px; line-height: 62.5px; letter-spacing: 0.4px;
    text-transform: uppercase;
  }
  .subtitle {
    position: absolute; left: 649px; top: 505px; z-index: 2;
    font-weight: 800; font-size: 15px; line-height: 18.2px; letter-spacing: 0.3px;
    text-transform: uppercase;
  }
</style>
</head>
<body>
<div class="cover">
  <div class="trim-frame"></div>

  <section class="back">
    <h2 class="back-heading">LEICHTER LEBEN MIT DER VELORIN DIÄT - GANZ EINFACH!</h2>
    <p class="back-text">Odignata quatem de consedi squiate<br>nullici te dio exerum cones et et pro mo<br>corro beat ex esequia quatis adipsapelis ut pa<br>ped mo quo ipsanditis aut volent dolore ma verumquiates<br>exeribus non et odi test eosa suntur sed ma volupti<br>dolenim incilla udisquas ex etur? Alitam aut qui ommo consedi tatio.</p>
    <p class="back-text">Hit volorro etus estibea vitia aliquid milita perioresto inusandis<br>volores et expero con excesci lleniti tem utem quunt earum volenti<br>nctorum, nis nonseque ellatur si dero earum velitiberes dolorae pora<br>dolut es nobitaerum fugitios magnitiam sum adis elluptat.</p>
    <p class="back-text spaced">Ant aliquid quat paritas aut vel il incillaccae parchit latis sam,<br>sum dunt ab idigenimet, ommolore porerio rernam aut libus et id<br>quuntem remporecti cones re none officitio il ipsunt quas venderist<br>que que ommolup itiurest lante omnimagnimo quiderem illabore<br>naturit et occusandita inctis dollupt atemodionse que cum que<br>volore volupti aspite erae.</p>
  </section>

  <div class="fold-line left"></div>
  <div class="fold-line right"></div>
  <div class="spine-text spine-author">HENRIKE SOLBECK</div>
  <div class="spine-text spine-title">LEICHTER LEBEN MIT DER VELORIN DIÄT – GANZ EINFACH!</div>

  <section class="front">
    <div class="cover-photo" role="img" aria-label="Foto einer schlanken Frau in grauer Unterwäsche mit weißer Umrisslinie einer früheren, fülligeren Silhouette"></div>
    <p class="author">HENRIKE SOLBECK</p>
    <h1 class="title">Leichter<br>leben mit<br>der Velorin<br>Diät –<br>ganz<br>einfach!</h1>
    <p class="subtitle">Gesunde und leckere Rezepte für jede Tageszeit<br>inkl. 14 Tage Ernährungsplan zur optimalen<br>Fettverbrennung und Gewichtsreduktion</p>
  </section>
</div>
</body>
</html>
```